Meridian Vault Data Systems Needs a Website Desing

We need a website design for a new company based in Kuwait called Meridian Vault Data Systems (MVDS). We provide Software as a Service (SaaS) solutions for small and medium business companies. We will develop the required E-systems like HR,Payroll,Accounting Systems for those customers who wants to focus on their business instead of wasting time to automate it. MVDS need a web site that represent this activity and showing our cloud products and allow out customers to easily identify their needs. as a normal web site basic things need to be included like :
about MVDS
Solutions
PressRoom
Contact us
please i need something similar to qorlix.com or tuv.com or www.hxp7zul.com with blue and black theme .. please check the Company's logo
hi all ,,,
the project is only design without any codes
Reason: The project is focus on design only ,, i will be really appreciated to have more designs

```html
<!DOCTYPE html>
<html lang="en">
<head>
<meta charset="utf-8">
<title>Meridian Vault Data Systems</title>
<link href="https://fonts.googleapis.com/css2?family=Play:wght@400;700&family=Roboto:wght@300;400&display=swap" rel="stylesheet">
<style>
:root{
  --blue:#1a8fd6;
  --blue-dark:#0f6fb3;
  --ink:#222;
  --text:#666;
  --dark:#1c1c1c;
  --darker:#141414;
  --strip:#eeeff1;
  --footer-text:#9fd0f3;
  --icon:#a4a8ad;
}
*{box-sizing:border-box;margin:0;padding:0}
html,body{width:1200px;height:990px;overflow:hidden;background:#fff}
body{font-family:'Roboto',Arial,sans-serif}
.page{position:relative;width:1400px;height:1155px;transform:scale(.857143);transform-origin:0 0;background:#fff}
.abs{position:absolute}

.topbar{left:0;top:0;width:1400px;height:72px;background:var(--darker)}
.topbar-contact{left:226px;top:13px;color:#fff;font-size:13px}
.btn{display:inline-block;background:linear-gradient(#3aa7ea,var(--blue-dark));color:#fff;border-radius:3px;font-size:14px;text-align:center;border:1px solid #0d5f99}
.btn-login{left:1022px;top:9px;width:70px;height:25px;line-height:23px}
.btn-register{left:1103px;top:9px;width:72px;height:25px;line-height:23px}

.hero{left:0;top:72px;width:1400px;height:428px;
  background:linear-gradient(180deg,#5d6f80 0%,#b69a6a 30%,#f2e1a8 52%,#c4bf5c 62%,#a7a933 78%,#8a9226 100%)}
.header{left:206px;top:44px;width:989px;height:72px;background:#fff;border-radius:3px;box-shadow:0 2px 6px rgba(0,0,0,.35)}
.brand{left:20px;top:10px;display:flex;align-items:center;gap:10px}
.brand-mark{width:50px;height:50px;border-radius:50%;background:var(--blue)}
.brand-name{font-family:'Play',sans-serif;font-weight:700;font-size:40px;color:#222}
.nav{right:22px;top:28px;display:flex;font-size:14px;color:#555}
.nav span{padding:0 23px;border-left:1px solid #ccc;line-height:14px}
.nav span:first-child{border:none;color:var(--blue);text-decoration:underline}
.nav span:last-child{padding-right:0}
.arrow{width:40px;height:40px;border-radius:50%;background:#2b2b2b}
.arrow-prev{left:184px;top:267px}
.arrow-next{left:1176px;top:267px}
.hero-title{left:604px;top:256px;font-family:'Play',sans-serif;font-weight:700;font-size:26px;color:var(--blue-dark)}
.hero-lede{left:605px;top:295px;width:500px;font-family:'Play',sans-serif;font-size:17px;line-height:23px;color:#2a2a2a}

.rule{left:0;top:500px;width:1400px;height:3px;background:var(--blue)}
.strip{left:0;top:503px;width:1400px;height:112px;background:var(--strip)}
.cat{top:510px;width:160px;height:96px;text-align:center;font-size:14px;color:#444;border-left:1px solid #dadcdf}
.cat:first-of-type{border-left:none}
.cat svg{display:block;margin:8px auto 6px}
.cat-active{color:#111}
.pointer{left:1089px;top:503px;width:0;height:0;border-left:12px solid transparent;border-right:12px solid transparent;border-top:10px solid var(--blue)}

.col{top:648px}
.col h2{font-weight:300;font-size:20px;color:#333;margin-bottom:12px}
.col p{font-size:12px;line-height:20px;color:var(--text);width:295px}
.list{list-style:none;font-size:12px;color:var(--text)}
.list li{line-height:23.7px;padding-left:23px;position:relative}
.list li::before{content:"";position:absolute;left:0;top:11px;width:7px;height:2px;background:var(--blue)}
.list li::after{content:"";position:absolute;left:5px;top:9px;border-left:4px solid var(--blue);border-top:3px solid transparent;border-bottom:3px solid transparent}
.btn-more{width:76px;height:28px;line-height:26px;font-size:12px}
.sep{top:655px;height:232px;border-left:1px dotted #aaa}

.footer{left:0;top:922px;width:1400px;height:191px;background:var(--dark)}
.footer h3{font-weight:400;font-size:17px;color:#fff;margin-bottom:13px}
.footer .list{color:var(--footer-text)}
.footer .list li{line-height:27px;font-size:12.5px}
.footer .list li::before{top:13px}.footer .list li::after{top:11px}
.fsep{top:940px;height:160px;border-left:1px solid #2c2c2c}
.news-text{font-size:12px;line-height:18px;color:var(--footer-text);width:220px}
.field{margin-top:10px;width:208px;height:29px;background:#6b6b6b;border-radius:3px;color:#ccc;font-size:12px;padding:7px 16px}
.btn-signup{margin-top:10px;width:76px;height:28px;line-height:26px;font-size:14px}
.contact-row{display:flex;align-items:center;gap:14px;font-size:12.5px;color:var(--footer-text);height:25px}
.social{display:flex;gap:8px;margin-top:4px}
.social span{width:30px;height:30px;border-radius:50%;background:var(--blue)}
.bottombar{left:0;top:1113px;width:1400px;height:42px;background:var(--darker);font-size:12.5px;color:var(--footer-text)}
</style>
</head>
<body>
<div class="page">
  <div class="abs topbar"></div>
  <div class="abs topbar-contact">Call us: (000) 000-0000 &nbsp; Email: info@qelvarin.com</div>
  <span class="abs btn btn-login">Login</span>
  <span class="abs btn btn-register">Register</span>

  <div class="abs hero" role="img" aria-label="Photo of a person with arms raised in a sunlit green field under a cloudy golden sky"></div>

  <div class="abs header">
    <div class="abs brand"><span class="brand-mark"></span><span class="brand-name">MVDS</span></div>
    <nav class="abs nav"><span>Home</span><span>About Us</span><span>Solutions</span><span>Services</span><span>Contact Us</span></nav>
  </div>

  <svg class="abs arrow arrow-prev" viewBox="0 0 40 40"><circle cx="20" cy="20" r="20" fill="#2b2b2b"/><path d="M23 12l-8 8 8 8" fill="none" stroke="#fff" stroke-width="2.5"/></svg>
  <svg class="abs arrow arrow-next" viewBox="0 0 40 40"><circle cx="20" cy="20" r="20" fill="#2b2b2b"/><path d="M17 12l8 8-8 8" fill="none" stroke="#fff" stroke-width="2.5"/></svg>
  <h1 class="abs hero-title">Meridian Vault Data Systems</h1>
  <p class="abs hero-lede">We provide Software as a Service (SaaS) solutions for small and medium business companies.</p>

  <div class="abs rule"></div>
  <div class="abs strip"></div>
  <div class="abs pointer"></div>

  <div class="abs cat" style="left:220px">
    <svg width="40" height="56" viewBox="0 0 40 56"><path d="M20 3a16 16 0 0 0-9 29v8h18v-8A16 16 0 0 0 20 3z" fill="none" stroke="var(--icon)" stroke-width="3"/><rect x="12" y="43" width="16" height="8" rx="2" fill="var(--icon)"/><path d="M14 18h5l3-6v6h4v9h-12z" fill="var(--blue)"/></svg>Software solutions</div>
  <div class="abs cat" style="left:380px">
    <svg width="50" height="56" viewBox="0 0 50 56"><circle cx="25" cy="17" r="12" fill="var(--icon)"/><path d="M4 54c0-14 9-22 21-22s21 8 21 22z" fill="var(--icon)"/><rect x="23" y="33" width="4" height="18" fill="var(--blue)"/></svg>HR Payroll</div>
  <div class="abs cat" style="left:540px">
    <svg width="56" height="56" viewBox="0 0 56 56"><circle cx="28" cy="28" r="23" fill="none" stroke="var(--icon)" stroke-width="5"/><path d="M6 25q22-10 44 0" fill="none" stroke="var(--icon)" stroke-width="5"/><circle cx="28" cy="30" r="7" fill="var(--icon)"/><path d="M23 28h10l-5 7z" fill="var(--blue)"/></svg>Consumer Auto</div>
  <div class="abs cat" style="left:700px">
    <svg width="62" height="56" viewBox="0 0 62 56"><path d="M31 52L7 28A13 13 0 0 1 31 10a13 13 0 0 1 24 18z" fill="var(--icon)"/><path d="M4 30h14l3-6 4 12 4-16 4 14 3-6h22" fill="none" stroke="var(--blue)" stroke-width="2"/></svg>Healthcare</div>
  <div class="abs cat" style="left:860px">
    <svg width="44" height="56" viewBox="0 0 44 56"><rect x="3" y="3" width="38" height="50" rx="6" fill="none" stroke="var(--icon)" stroke-width="4"/><rect x="10" y="10" width="24" height="7" fill="var(--blue)"/><g fill="var(--blue)"><circle cx="13" cy="25" r="2.5"/><circle cx="22" cy="25" r="2.5"/><circle cx="31" cy="25" r="2.5"/><circle cx="13" cy="33" r="2.5"/><circle cx="22" cy="33" r="2.5"/><circle cx="31" cy="33" r="2.5"/><circle cx="13" cy="41" r="2.5"/><circle cx="22" cy="41" r="2.5"/><circle cx="31" cy="41" r="2.5"/></g></svg>Accounting</div>
  <div class="abs cat cat-active" style="left:1020px">
    <svg width="72" height="56" viewBox="0 0 72 56"><path d="M36 28c-8-10-14-15-21-15a15 15 0 0 0 0 30c7 0 13-5 21-15s14-15 21-15a15 15 0 0 1 0 30c-7 0-13-5-21-15z" fill="none" stroke="var(--blue)" stroke-width="6"/></svg>Solutions For All</div>

  <section class="abs col" style="left:225px">
    <h2>What is MVDS?</h2>
    <p>Lorem ipsum dolor sit amet, consectetur adipisicing elit esed do eiusmod tempor incididunt ut labore et dolore magna aliqua. Ut enim ad minim veniam, quis nostrud exercitation ullamco laboris nisi ut aliqup ex ea commo esed do eiusmod tempor incididunt ut labore et dolore magna aliqua. Ut enim ad minim veniam, quis nostrud exercitation ullamco laboris nisi ut aliqup ex ea commo voluptate velit esse cillum</p>
  </section>
  <span class="abs btn btn-more" style="left:226px;top:857px">Read More</span>
  <div class="abs sep" style="left:545px"></div>

  <section class="abs col" style="left:574px">
    <h2>Benefits Using SaaS</h2>
    <ul class="list"><li>Affordable</li><li>Quick to Deploy</li><li>Zero Infrastructure</li><li>Seamless Upgrades</li><li>Guaranteed Levels of Service</li><li>Backups and Data Recovery all done for you</li><li>Work Anywhere</li></ul>
  </section>
  <span class="abs btn btn-more" style="left:575px;top:857px">Read More</span>
  <div class="abs sep" style="left:860px"></div>

  <section class="abs col" style="left:886px">
    <h2>Why Choose MVDS?</h2>
    <ul class="list"><li>Lorem ipsum dolor sit amet, consectetur adipisicing</li><li>Lorem ipsum dolor sit amet, consectetur adipisicing</li><li>Lorem ipsum dolor sit amet, consectetur adipisicing</li><li>Lorem ipsum dolor sit amet, consectetur adipisicing</li><li>Lorem ipsum dolor sit amet, consectetur adipisicing</li><li>Lorem ipsum dolor sit amet, consectetur adipisicing</li><li>Lorem ipsum dolor sit amet, consectetur adipisicing</li></ul>
  </section>
  <span class="abs btn btn-more" style="left:886px;top:857px">Read More</span>

  <footer class="abs footer">
    <div class="abs" style="left:225px;top:18px"><h3>Usefull Links</h3><ul class="list"><li>Home</li><li>About Us</li><li>Solutions</li><li>Contact Us</li></ul></div>
    <div class="abs" style="left:437px;top:18px"><h3>Services</h3><ul class="list"><li>Lorem Ipsum Dolor</li><li>Lorem Ipsum Dolor</li><li>Lorem Ipsum Dolor</li><li>Lorem Ipsum Dolor</li><li>Lorem Ipsum Dolor</li></ul></div>
    <div class="abs" style="left:681px;top:18px"><h3>Newsletter</h3><p class="news-text">Lorem ipsum dolor sit amet, consectetur adipisicing elit, sed do.</p><div class="field">Enter Your Email</div><span class="btn btn-signup">Signup</span></div>
    <div class="abs" style="left:1005px;top:18px">
      <h3 style="margin-bottom:8px">Contact Us</h3>
      <div class="contact-row"><svg width="16" height="20" viewBox="0 0 16 20"><rect x="3" y="1" width="10" height="18" rx="2" fill="var(--blue)"/><rect x="5" y="4" width="6" height="9" fill="var(--dark)"/></svg>(000) 000 0000</div>
      <div class="contact-row"><svg width="16" height="16" viewBox="0 0 16 16"><rect x="1" y="4" width="14" height="11" fill="var(--blue)"/><path d="M1 4l7 6 7-6" fill="none" stroke="var(--dark)" stroke-width="1.5"/></svg>info@qelvarin.com</div>
      <h3 style="margin:14px 0 6px">Show Some Love</h3>
      <div class="social"><span></span><span></span><span></span></div>
    </div>
  </footer>
  <div class="abs fsep" style="left:379px"></div>
  <div class="abs fsep" style="left:624px"></div>
  <div class="abs fsep" style="left:951px"></div>

  <div class="abs bottombar"><span class="abs" style="left:225px;top:14px">Privacy Policy</span><span class="abs" style="left:1094px;top:14px">Copyright 2013</span></div>
</div>
</body>
</html>
```